Health Coach needs a creative and catchy Muralto Ad Image to increase page likes

I have just recently launched a health coaching business and would like to increase my Muralto awareness and page likes.
I plan on doing a “page liking” campaign through Muralto and want a creative, catchy and unique image to help make my campaign successful.
I want a versatile image, as I am aiming to run this campaign on Muralto for a while (few months).
The image is to be 1200 x 444 pixels, with an image ratio of 8:3, and because it is going on Muralto it cannot have any overlaid text (or very little).
So, the image will have to be very visually appealing and catchy!
I am happy for some creative illustrations and drawings to be used to help portray my message (please see attached for some sample pictures)
I would like the image to portray the following:
-health
-happiness
-change
Some of my key messages that you could include:
-holistic health
-health & wellness
-health, nutrition, lifestyle
-Food, fitness, happiness

In addition, a call to action that could be incorporated could be:
"i can help you"
..or something similar (but only if this can fit).

I have attached some images of myself to be used.

Target Market(s)

People looking for health and fitness advice

Industry/Entity Type

Health And Wellness

Colors

Designer to choose colors to be used in the design.

Requirements
Nice to have
• illustrations as per 2 sample images provided
• call to action if can fit

```html
<!DOCTYPE html>
<html lang="en">
<head>
<meta charset="utf-8">
<title>I Can Help You – Health Coaching</title>
<link rel="stylesheet" href="https://fonts.googleapis.com/css2?family=Dosis:wght@700&family=Tenor+Sans&display=swap">
<style>
  :root {
    --navy-deep: #173a6b;
    --navy-light: #3c6ea8;
    --amber: #eda12a;
    --headline: #f8cf8e;
    --cream: #fdf5cf;
    --sky: #f3f2ea;
    --hill: #8a9a6c;
    --sea: #c9d6de;
    --rock: #b9a48d;
  }
  html, body {
    margin: 0;
    padding: 0;
    overflow: hidden;
    background: #ffffff;
  }
  .banner {
    position: relative;
    width: 1200px;
    height: 444px;
    overflow: hidden;
  }
  .banner__photo {
    position: absolute;
    left: 430px;
    top: 0;
    width: 770px;
    height: 444px;
    background:
      linear-gradient(180deg,
        var(--sky) 0%,
        #dfe0cf 18%,
        var(--hill) 36%,
        var(--sea) 52%,
        #d8dde0 62%,
        var(--rock) 78%,
        #a99580 100%);
  }
  .banner__shapes {
    position: absolute;
    left: 0;
    top: 0;
  }
  .banner__copy {
    position: absolute;
    left: 40px;
    top: 112px;
  }
  .headline {
    margin: 0 0 26px;
    font-family: "Dosis", sans-serif;
    font-weight: 700;
    font-size: 47px;
    letter-spacing: 1.5px;
    line-height: 1;
    color: var(--headline);
  }
  .messages {
    list-style: none;
    margin: 0;
    padding: 0;
    font-family: "Tenor Sans", sans-serif;
    font-variant: small-caps;
    text-transform: lowercase;
    font-size: 25px;
    line-height: 34px;
    color: var(--cream);
    letter-spacing: 0.5px;
  }
  .messages .amp {
    font-size: 30px;
  }
</style>
</head>
<body>
  <div class="banner">
    <div class="banner__photo" role="img" aria-label="Photo of the health coach standing on coastal rocks beside an ocean pool in warm sunlight"></div>

    <svg class="banner__shapes" width="1200" height="444" viewBox="0 0 1200 444" aria-hidden="true">
      <defs>
        <radialGradient id="panelGlow" cx="0.3" cy="0.45" r="0.75">
          <stop offset="0" stop-color="var(--navy-light)"/>
          <stop offset="1" stop-color="var(--navy-deep)"/>
        </radialGradient>
      </defs>
      <polygon class="panel" points="0,0 435,0 525,218 435,444 0,444" fill="url(#panelGlow)"/>
      <polygon class="chevron chevron--top" points="435,0 568,150 522,204" fill="var(--amber)"/>
      <polygon class="chevron chevron--bottom" points="522,236 570,283 435,444" fill="var(--amber)"/>
    </svg>

    <div class="banner__copy">
      <h1 class="headline">I CAN HELP YOU</h1>
      <ul class="messages">
        <li>Holistic Health</li>
        <li>Health <span class="amp">&amp;</span> amp Wellness</li>
        <li>Health, Nutrition, Lifestyle</li>
        <li>Food, Fitness, Happiness</li>
      </ul>
    </div>
  </div>
</body>
</html>
```